Web design for sitter site

We will be launching a sitter site in the coming months that focuses on sitters for children. The name of this site will be KinWatch.com
We will need:
1. main page design
2. site logo designed
3. subpages as well for the look of people's profiles, and job listings, etc (see links below)
We only need the design, photos, font files, etc. We do not need this site coded (no html), a ps job is fine.
Some competing sites in the space include - tendhaven.com and mindly.com
http://www.example-guardia.com/images/profile1.jpg
http://brookvaleshelf.example/wp-content/uploads/2013/09/mindly-review.png
http://www.pinecrestuni.example/hr/photos/tend_haven2.jpg
Thanks for your interest!
Target Market(s)
Mothers of children, mainly women
Industry/Entity Type
Online
Look and feel

```html
<!DOCTYPE html>
<html lang="en">
<head>
<meta charset="utf-8">
<title>KinWatch.com – Find a Babysitter</title>
<link href="https://fonts.googleapis.com/css2?family=Open+Sans:ital,wght@0,400;0,600;0,700;1,400&family=Arimo:ital,wght@0,400;0,700;1,400;1,700&display=swap" rel="stylesheet">
<style>
:root{
  --navy:#13233f;
  --navy-deep:#0f1d35;
  --green:#2aa887;
  --green-dark:#1f8c70;
  --blue:#1a73c9;
  --blue-dark:#0f5aa6;
  --text:#333;
  --muted:#666;
  --light:#f3f3f3;
  --line:#d8d8d8;
  --footer-top:#1c3356;
  --footer-bottom:#41658a;
}
*{box-sizing:border-box;margin:0;padding:0}
html,body{width:1200px;height:2308px;overflow:hidden}
body{position:relative;font-family:"Arimo",Arial,sans-serif;color:var(--text);background:#fff}

/* header */
.site-header{position:absolute;left:0;top:0;width:1200px;height:88px;background:var(--navy)}
.brand{position:absolute;left:138px;top:26px;display:flex;align-items:center;gap:10px}
.brand-dot{width:16px;height:16px;border-radius:50%;background:#fff}
.brand-name{font-family:"Open Sans",sans-serif;font-weight:700;font-size:27px;color:#fff;letter-spacing:-.5px}
.slogan{position:absolute;left:366px;top:38px;padding-left:9px;border-left:1px solid #3d5275;font-size:14px;color:#6f82a3;line-height:18px}
.signup-links{position:absolute;left:748px;top:31px;width:209px;height:34px;border:1px solid #7c8ba6;display:flex;align-items:center;justify-content:center;gap:10px;font-size:15px;color:#fff}
.signup-links .label,.signup-links .sep{color:#8b9ab3}
.login-btn{position:absolute;left:972px;top:31px;width:88px;height:34px;border-radius:3px;background:linear-gradient(#35b894,var(--green-dark));color:#fff;font-family:"Open Sans",sans-serif;font-weight:600;font-size:17px;text-align:center;line-height:34px}

/* hero */
.hero-photo{position:absolute;left:0;top:88px;width:1200px;height:720px;background:linear-gradient(100deg,#e9e4dc 0%,#d9d2c6 35%,#ece8e2 60%,#f1eee8 100%)}
.signup-card{position:absolute;left:635px;top:274px;width:427px;height:517px;background:rgba(255,255,255,.9);border:1px solid #c9c9c9;box-shadow:0 0 6px rgba(0,0,0,.12)}
.signup-card h2{position:absolute;left:24px;top:22px;font-family:"Open Sans",sans-serif;font-weight:600;font-size:27px;color:var(--green)}
.signup-card .lead{position:absolute;left:24px;top:66px;width:340px;font-size:15px;line-height:18px;color:#555}
.signup-card .lead b{color:var(--green)}
.role-choice{position:absolute;left:22px;top:134px;display:flex;gap:28px;font-family:"Open Sans",sans-serif;font-weight:600;font-size:20px;color:#555}
.role-choice span{display:flex;align-items:center;gap:6px}
.radio{width:13px;height:13px;border-radius:50%;border:1px solid #888;background:#eee}
.field{position:absolute;height:36px;border:1px solid #c7c7c7;border-radius:3px;background:#fff;font-size:14px;color:#aaa;line-height:34px;padding-left:12px}
.agree{position:absolute;left:26px;top:368px;width:380px;display:flex;gap:12px;font-size:12px;line-height:20px;color:#555}
.agree .box{flex:none;width:12px;height:12px;margin-top:4px;border:1px solid #999;background:#eee}
.agree a{color:var(--blue);text-decoration:none}
.join-btn{position:absolute;left:19px;top:438px;width:386px;height:37px;border-radius:3px;background:linear-gradient(#2f8ee0,var(--blue-dark));color:#fff;font-size:17px;text-align:center;line-height:37px;border:1px solid #0c4d8f}

/* testimonial */
.testimonial{position:absolute;left:0;top:808px;width:1200px;height:189px;background:#fff}
.quote-mark{position:absolute;left:138px;top:14px}
.slider-arrows{position:absolute;left:995px;top:15px;display:flex;gap:3px}
.slider-arrows span{width:26px;height:19px;background:#a6a6a6;display:flex;align-items:center;justify-content:center}
.slider-arrows span.next{background:#1d1d1d}
.testimonial blockquote{position:absolute;left:175px;top:53px;width:850px;text-align:center;font-style:italic;font-size:15.5px;line-height:22.5px;color:#666}
.testimonial cite{position:absolute;left:0;top:141px;width:1200px;text-align:center;font-style:italic;font-weight:700;font-size:15px;color:#555}

/* how it works */
.how-it-works{position:absolute;left:0;top:997px;width:1200px;height:445px;background:var(--navy)}
.video-frame{position:absolute;left:138px;top:21px;width:634px;height:393px;border-radius:38px;background:#fff;box-shadow:0 8px 14px rgba(0,0,0,.35)}
.video-still{position:absolute;left:36px;top:22px;width:566px;height:351px;background:linear-gradient(110deg,#f4efe6 0%,#e8c9b4 40%,#b88469 62%,#cfd9c9 100%)}
.play-icon{position:absolute;left:276px;top:131px}
.how-copy{position:absolute;left:797px;top:29px;color:#fff;font-family:"Open Sans",sans-serif}
.how-copy h3{font-weight:600;font-size:21px}
.how-copy .watch{font-size:16px;margin-top:2px}
.how-copy .dots{width:211px;border-top:2px dotted #a8b6cc;margin-top:14px}
.how-copy .pitch{margin-top:14px;font-weight:700;font-size:16px;line-height:21px}
.cta{position:absolute;left:822px;width:155px;height:44px;border-radius:10px;color:#fff;font-family:"Open Sans",sans-serif;font-weight:600;font-size:17px;text-align:center;line-height:44px;box-shadow:0 3px 5px rgba(0,0,0,.35)}
.cta.parents{top:201px;background:linear-gradient(#38bb95,var(--green-dark))}
.cta.sitters{top:255px;background:linear-gradient(#2a8ee2,var(--blue-dark))}

/* sitter info */
.sitter-info{position:absolute;left:0;top:1442px;width:1200px;height:600px;background:var(--light)}
.section-title{position:absolute;top:27px;font-family:"Open Sans",sans-serif;font-weight:600;font-size:19.5px;color:#444}
.steps{position:absolute;left:138px;top:69px;list-style:none}
.step{position:relative;width:385px;height:58px;margin-bottom:17.4px;background:linear-gradient(#fff,#f0f0f0);border:1px solid #e3e3e3;border-radius:3px;box-shadow:0 1px 2px rgba(0,0,0,.06);padding:12px 0 0 27px}
.step::before{content:"";position:absolute;left:10px;top:20px;border-left:7px solid #1a73c9;border-top:4.5px solid transparent;border-bottom:4.5px solid transparent}
.step h4{font-size:15.5px;font-weight:400;color:#222;line-height:18px}
.step p{font-size:12.5px;color:#555;line-height:17px}
.divider{position:absolute;left:607px;top:46px;width:1px;height:504px;background:#e1e1e1}
.requirements{position:absolute;left:697px;top:92px;width:365px}
.requirements h5{font-weight:400;font-size:15.5px;color:#222;margin-bottom:6px}
.requirements ul{list-style:none;margin-bottom:19px}
.requirements li{display:flex;align-items:center;gap:7px;font-size:12.5px;color:#444;margin:0 0 8px 16px}
.requirements li .bullet{width:10px;height:10px;border-radius:50%;border:1px solid #555;position:relative}
.requirements li .bullet::after{content:"";position:absolute;left:2px;top:2px;width:4px;height:4px;border-radius:50%;background:#555}
.requirements .note{font-size:13px;line-height:19px;color:#444;margin-top:24px}
.requirements .ps{margin-top:26px;padding-top:8px;border-top:1px dashed #999;font-style:italic;font-size:12.5px;line-height:19px;color:#555}

/* footer */
.site-footer{position:absolute;left:0;top:2042px;width:1200px;height:266px;background:linear-gradient(var(--footer-top),var(--footer-bottom))}
.footer-col{position:absolute;top:30px}
.footer-col h6{font-family:"Open Sans",sans-serif;font-weight:600;font-size:15.5px;color:#fff;margin-bottom:6px}
.footer-col a{display:block;font-size:12px;line-height:21.5px;color:#b9c6da;text-decoration:none}
.newsletter input{display:block;width:171px;height:26px;border:1px solid #8ea2bf;border-radius:2px;margin-bottom:9px;padding-left:6px;font-family:inherit;font-size:12px;color:#222;background:#fff}
.newsletter .send{margin-left:100px;width:71px;height:24px;border-radius:5px;border:1px solid #0a3f78;background:linear-gradient(#2c8ee0,var(--blue-dark));color:#fff;font-weight:700;font-size:12.5px;text-align:center;line-height:22px}
.social{display:flex;gap:6px}
.social span{width:33px;height:33px;border-radius:2px}
.social .s1{background:#3b5a99}.social .s2{background:#2ba4dc}.social .s3{background:#cc2b22}.social .s4{background:#d8442f}
.like-count{margin-top:9px;display:flex;gap:4px;align-items:center}
.like-count .pill{width:40px;height:18px;border-radius:2px;background:#4a69a6}
.like-count .num{height:18px;padding:0 5px;background:#fff;border:1px solid #ccc;font-size:11px;color:#333;line-height:16px}
.copyright{position:absolute;left:140px;top:191px;font-size:12px;color:#fff}
</style>
</head>
<body>

<header class="site-header">
  <div class="brand"><span class="brand-dot"></span><span class="brand-name">KinWatch.com</span></div>
  <div class="slogan">The Slogan Goes Here</div>
  <nav class="signup-links"><span class="label">Sign Up</span><span class="sep">:</span><span>Parents</span><span class="sep">|</span><span>Sitters</span></nav>
  <div class="login-btn">Login</div>
</header>

<section class="hero-photo" role="img" aria-label="Mother lying on a carpet drawing with crayons alongside a toddler and a baby"></section>

<form class="signup-card">
  <h2>Sign Up Now!</h2>
  <p class="lead">Sign up to start your <b>FREE</b> search for babysitters in your area.</p>
  <div class="role-choice"><span><i class="radio"></i>I’m a parent</span><span><i class="radio"></i>I’m a babysitter</span></div>
  <div class="field" style="left:24px;top:177px;width:383px">Name</div>
  <div class="field" style="left:24px;top:220px;width:383px">Email Address</div>
  <div class="field" style="left:24px;top:263px;width:187px">Password</div>
  <div class="field" style="left:219px;top:263px;width:188px">Confirm Password</div>
  <div class="field" style="left:24px;top:305px;width:383px">Zip Code or City, State</div>
  <div class="agree"><span class="box"></span><span>I agree to the <a>Terms of Use</a>. For details on collection and use of your information, see our <a>Privacy Policy</a>.</span></div>
  <div class="join-btn">Join KinWatch Club Now</div>
</form>

<section class="testimonial">
  <svg class="quote-mark" width="32" height="26" viewBox="0 0 32 26"><path d="M0 26V14C0 6 4 1 12 0v5C7 6 6 9 6 12h7v14zM18 26V14c0-8 4-13 12-14v5c-5 1-6 4-6 7h7v14z" fill="#8a8a8a"/></svg>
  <div class="slider-arrows">
    <span><svg width="8" height="10"><path d="M6 1 2 5l4 4" stroke="#fff" stroke-width="2" fill="none"/></svg></span>
    <span class="next"><svg width="8" height="10"><path d="M2 1l4 4-4 4" stroke="#fff" stroke-width="2" fill="none"/></svg></span>
  </div>
  <blockquote>This is our third year using KinWatch.com Babysitting and the sitters are wonderful.&nbsp; The thing I notice the most is how happy they appear – they behave as if they were looking forward all day to playing with our child.&nbsp; The sitters have been on time, courteous, professional and very sweet to our son.&nbsp; We will continue to use this service and highly recommend!</blockquote>
  <cite>– Hanna and Tomas</cite>
</section>

<section class="how-it-works">
  <div class="video-frame">
    <div class="video-still" role="img" aria-label="Video still of a mother and toddler drawing together at a table">
      <svg class="play-icon" width="86" height="86" viewBox="0 0 86 86"><circle cx="43" cy="43" r="40" fill="rgba(255,255,255,.25)" stroke="#fff" stroke-width="4"/><path d="M34 25l26 18-26 18z" fill="#fff"/></svg>
    </div>
  </div>
  <div class="how-copy">
    <h3>How KinWatch.com Works</h3>
    <p class="watch">Watch the video »</p>
    <div class="dots"></div>
    <p class="pitch">Sign up to start your<br>babysitter search for free.</p>
  </div>
  <div class="cta parents">PARENTS</div>
  <div class="cta sitters">SITTERS</div>
</section>

<section class="sitter-info">
  <h3 class="section-title" style="left:138px">WANT TO BE A SITTER?</h3>
  <ol class="steps">
    <li class="step"><h4>SIGN UP</h4><p>Create an account it’s simple.</p></li>
    <li class="step"><h4>CHOOSE PACKAGE</h4><p>Choose how many months suitable for you!</p></li>
    <li class="step"><h4>LET US CHECK YOU OUT!</h4><p>Safety and trust are very important to us.</p></li>
    <li class="step"><h4>WATCH VIDEOS</h4><p>We’ll teach youhow to be the BEST SITTER.</p></li>
    <li class="step"><h4>ACCEPT JOBS</h4><p>The faster you respond the better!</p></li>
    <li class="step"><h4>HAVE FUN WITH KIDS</h4><p>We can give&nbsp; you plenty of ideas.</p></li>
    <li class="step"><h4>GET PAID</h4><p>Effectively paid online, attain reviews and find more work.</p></li>
  </ol>
  <div class="divider"></div>
  <h3 class="section-title" style="left:697px">TO BE PART OF KinWatch.com</h3>
  <div class="requirements">
    <h5>1. WE HAVE TO CHECK YOU OUT.</h5>
    <ul>
      <li><i class="bullet"></i>National Federal Police Check</li>
      <li><i class="bullet"></i>State based working with children cares</li>
      <li><i class="bullet"></i>Drivers Licence / Visa</li>
    </ul>
    <h5>2. IT’S GOOD IDEA TO ATTAIN</h5>
    <ul>
      <li><i class="bullet"></i>Personal insurance</li>
      <li><i class="bullet"></i>CPR training</li>
      <li><i class="bullet"></i>ABN</li>
    </ul>
    <p class="note">We will help you get organised and working in 5 days as long as there are no nasties!</p>
    <p class="ps">P.S If candidates accept / respond to bookings fast can they climb up to the top of the page. eg. like a search ranking.</p>
  </div>
</section>

<footer class="site-footer">
  <div class="footer-col" style="left:140px"><h6>Company</h6><a>About Us</a><a>FAQs &amp; Support</a><a>Terms of Service</a><a>Privacy Policy</a></div>
  <div class="footer-col" style="left:331px"><h6>Quick Links</h6><a>Parents</a><a>Babysitters</a><a>How it Works</a><a>Careers at KinWatch Club</a><a>Contact Us</a></div>
  <div class="footer-col" style="left:514px"><h6>My Account</h6><a>Register</a><a>Login</a></div>
  <div class="footer-col newsletter" style="left:694px;top:28px"><h6>Newsletter Sign Up</h6><input value="Your Name" readonly><input value="Email Address" readonly><div class="send">Sign Up</div></div>
  <div class="footer-col" style="left:897px"><h6>Join us on</h6>
    <div class="social"><span class="s1"></span><span class="s2"></span><span class="s3"></span><span class="s4"></span></div>
    <div class="like-count"><span class="pill"></span><span class="num">191k</span></div>
  </div>
  <p class="copyright">© 2014 KinWatch.com. All Rights Reserved.</p>
</footer>

</body>
</html>
```